One business card required with 2 company logos and 2 people's details

One business card required.
No preference on design - One side could show the 2 different business logos for the companies we own. The reverse could have the details shown below.
Another option could be one business one side and one business on the reverse. Happy to receive designs.

Karen Wibberley
07700 913 258
Joanna Pettifer
07700 927 341

website: truelymarvellous.example
email: info@truelymarvellous.example

website: ironheronoccasions.example
email: info:ironheronoccasions.example

May be nice to have icons instead of the words email/website?

I have included different versions of the logos to help with your design.

Contact Information for Business Card

see project overview

Requirements
Must have
• both company logos, both contact names and contact details

```html
<!DOCTYPE html>
<html lang="en">
<head>
<meta charset="utf-8">
<title>Business cards – Iron Heron Occasions &amp; Truely Marvellous</title>
<link rel="stylesheet" href="https://fonts.googleapis.com/css2?family=Jost:ital,wght@0,400;0,500;1,400&family=Petit+Formal+Script&family=Vollkorn:wght@400&display=swap">
<style>
  :root {
    --page-bg: #2a2a2b;
    --card-white: #ffffff;
    --heron-blue-light: #0a78bd;
    --heron-blue-deep: #1d2671;
    --heron-band: #0b8fcf;
    --heron-logo: #1a64d6;
    --marvel-violet: #6459c4;
    --marvel-sky: #4f9ae0;
    --marvel-cyan: #5fd8e6;
    --marvel-band-end: #3a56c4;
    --marvel-logo: #2c2a55;
    --text-on-panel: #ffffff;
  }
  * { box-sizing: border-box; margin: 0; padding: 0; }
  html, body {
    width: 1125px; height: 1200px; overflow: hidden;
    background: var(--page-bg);
  }
  .sheet { position: relative; width: 1125px; height: 1200px; }
  .card {
    position: absolute; left: 150px; width: 826px; height: 471px;
    background: var(--card-white);
    overflow: hidden;
  }
  .card--heron { top: 98px; }
  .card--marvel { top: 631px; }
  .card__panel { position: absolute; inset: 0; width: 100%; height: 100%; }
  .contacts {
    position: absolute; left: 44px;
    color: var(--text-on-panel);
    font-family: "Jost", sans-serif;
  }
  .card--heron .contacts { top: 124px; }
  .card--marvel .contacts { top: 146px; left: 33px; }
  .person__name { display: block; line-height: 1; }
  .card--heron .person__name {
    font-family: "Vollkorn", serif; font-size: 31px; font-weight: 400;
  }
  .card--marvel .person__name {
    font-family: "Petit Formal Script", cursive; font-size: 27px;
  }
  .person__phone {
    display: flex; align-items: center; gap: 6px;
    font-size: 20px; letter-spacing: 0.5px; margin-top: 8px;
  }
  .person + .person { margin-top: 26px; }
  .card--marvel .person + .person { margin-top: 24px; }
  .links { margin-top: 20px; font-size: 18px; font-style: italic; }
  .links__row { display: flex; align-items: center; gap: 9px; line-height: 25px; white-space: nowrap; }
  .icon { width: 15px; height: 15px; fill: currentColor; flex: none; }
  .brand {
    position: absolute; text-align: center; line-height: 1.05;
  }
  .brand--heron {
    left: 470px; width: 300px; top: 190px;
    font-family: "Vollkorn", serif; font-size: 40px;
    color: var(--heron-logo); letter-spacing: 1px;
  }
  .brand--marvel {
    left: 460px; width: 310px; top: 185px;
    font-family: "Jost", sans-serif; font-size: 40px; font-weight: 400;
    color: var(--marvel-logo);
  }
</style>
</head>
<body>
<main class="sheet">

  <section class="card card--heron" aria-label="Iron Heron Occasions card">
    <svg class="card__panel" viewBox="0 0 800 457" preserveAspectRatio="none" aria-hidden="true">
      <defs>
        <linearGradient id="heronPanel" x1="0" y1="0" x2="1" y2="0">
          <stop offset="0" stop-color="var(--heron-blue-light)"/>
          <stop offset="0.75" stop-color="var(--heron-blue-deep)"/>
        </linearGradient>
      </defs>
      <path d="M0 0 H352 C338 70 362 160 384 250 C404 335 414 400 392 457 H0 Z" fill="var(--heron-band)"/>
      <path d="M0 0 H345 C332 70 352 160 372 250 C390 335 396 400 360 457 H0 Z" fill="url(#heronPanel)"/>
    </svg>

    <div class="contacts">
      <div class="person">
        <span class="person__name">Joanna Pettifer</span>
        <span class="person__phone"><svg class="icon" viewBox="0 0 24 24"><path d="M6.6 10.8a15.1 15.1 0 0 0 6.6 6.6l2.2-2.2a1 1 0 0 1 1-.25 11.4 11.4 0 0 0 3.6.57 1 1 0 0 1 1 1V20a1 1 0 0 1-1 1A17 17 0 0 1 3 4a1 1 0 0 1 1-1h3.5a1 1 0 0 1 1 1c0 1.25.2 2.45.57 3.57a1 1 0 0 1-.25 1z"/></svg>07700 927 341</span>
      </div>
      <div class="person">
        <span class="person__name">Karen Wibberley</span>
        <span class="person__phone"><svg class="icon" viewBox="0 0 24 24"><path d="M6.6 10.8a15.1 15.1 0 0 0 6.6 6.6l2.2-2.2a1 1 0 0 1 1-.25 11.4 11.4 0 0 0 3.6.57 1 1 0 0 1 1 1V20a1 1 0 0 1-1 1A17 17 0 0 1 3 4a1 1 0 0 1 1-1h3.5a1 1 0 0 1 1 1c0 1.25.2 2.45.57 3.57a1 1 0 0 1-.25 1z"/></svg>07700 913 258</span>
      </div>
      <div class="links">
        <div class="links__row"><svg class="icon" viewBox="0 0 24 24"><path d="M2 5h20v14H2z M3.5 6.5 12 13l8.5-6.5" fill="none" stroke="currentColor" stroke-width="2"/></svg>info@ironheronoccasions.example</div>
        <div class="links__row"><svg class="icon" viewBox="0 0 24 24"><circle cx="12" cy="12" r="10"/><path d="M7 7c2 0 3 1 3 3s-2 2-2 4 2 2 2 5M14 4c0 2 2 3 3 3s2 2 1 4" fill="none" stroke="var(--heron-blue-deep)" stroke-width="1.6"/></svg>ironheronoccasions.example</div>
      </div>
    </div>

    <div class="brand brand--heron">Iron Heron<br>Occasions</div>
  </section>

  <section class="card card--marvel" aria-label="Truely Marvellous card">
    <svg class="card__panel" viewBox="0 0 800 457" preserveAspectRatio="none" aria-hidden="true">
      <defs>
        <radialGradient id="marvelPanel" cx="0.22" cy="0.42" r="0.6">
          <stop offset="0" stop-color="var(--marvel-sky)"/>
          <stop offset="1" stop-color="var(--marvel-violet)"/>
        </radialGradient>
        <linearGradient id="marvelBand" x1="0" y1="0" x2="0" y2="1">
          <stop offset="0" stop-color="var(--marvel-cyan)"/>
          <stop offset="1" stop-color="var(--marvel-band-end)"/>
        </linearGradient>
      </defs>
      <path d="M0 0 H368 C322 40 314 110 346 190 C384 285 432 370 398 457 H0 Z" fill="url(#marvelBand)"/>
      <path d="M0 0 H330 C298 40 296 110 326 190 C364 285 418 370 386 457 H0 Z" fill="url(#marvelPanel)"/>
    </svg>

    <div class="contacts">
      <div class="person">
        <span class="person__name">Joanna Pettifer</span>
        <span class="person__phone"><svg class="icon" viewBox="0 0 24 24"><path d="M6.6 10.8a15.1 15.1 0 0 0 6.6 6.6l2.2-2.2a1 1 0 0 1 1-.25 11.4 11.4 0 0 0 3.6.57 1 1 0 0 1 1 1V20a1 1 0 0 1-1 1A17 17 0 0 1 3 4a1 1 0 0 1 1-1h3.5a1 1 0 0 1 1 1c0 1.25.2 2.45.57 3.57a1 1 0 0 1-.25 1z"/></svg>07700 927 341</span>
      </div>
      <div class="person">
        <span class="person__name">Karen Wibberley</span>
        <span class="person__phone"><svg class="icon" viewBox="0 0 24 24"><path d="M6.6 10.8a15.1 15.1 0 0 0 6.6 6.6l2.2-2.2a1 1 0 0 1 1-.25 11.4 11.4 0 0 0 3.6.57 1 1 0 0 1 1 1V20a1 1 0 0 1-1 1A17 17 0 0 1 3 4a1 1 0 0 1 1-1h3.5a1 1 0 0 1 1 1c0 1.25.2 2.45.57 3.57a1 1 0 0 1-.25 1z"/></svg>07700 913 258</span>
      </div>
      <div class="links">
        <div class="links__row"><svg class="icon" viewBox="0 0 24 24"><path d="M2 5h20v14H2z M3.5 6.5 12 13l8.5-6.5" fill="none" stroke="currentColor" stroke-width="2"/></svg>info@truelymarvellous.example</div>
        <div class="links__row"><svg class="icon" viewBox="0 0 24 24"><circle cx="12" cy="12" r="10"/><path d="M7 7c2 0 3 1 3 3s-2 2-2 4 2 2 2 5M14 4c0 2 2 3 3 3s2 2 1 4" fill="none" stroke="var(--marvel-violet)" stroke-width="1.6"/></svg>truelymarvellous.example</div>
      </div>
    </div>

    <div class="brand brand--marvel">Truely<br>Marvellous</div>
  </section>

</main>
</body>
</html>
```